Brightwave Reach - Business Card

We need a business card for a Social Media Marketing company that specializes in online marketing for small businesses in Canada using common Social Media platforms such as Pictora, Kinloop, Blinkit & Chirpo.

I have uploaded a copy of our logo which I would like utilized in the business card. We would like the business card to be modern yet classy design.

Our website is www.brightwavereach.ca

Industry/Entity Type

Marketing

Contact Information for Business Card

Email: info@brightwavereach.ca
Website: www.brightwavereach.ca
Telephone: 604-392-5108

Colors

Designer to choose colors to be used in the design.

Requirements
Must have
• Social Media icons on reverse
• Please add some designs with color.

```html
<!DOCTYPE html>
<html lang="en">
<head>
<meta charset="utf-8">
<title>Brightwave Reach – Business Card</title>
<link rel="stylesheet" href="https://fonts.googleapis.com/css2?family=Roboto:wght@400;500;700&display=swap">
<style>
  :root {
    --backdrop: #d8d3cc;
    --card: #3c4245;
    --ink: #ffffff;
    --ink-soft: #e6e8e9;
  }
  * { box-sizing: border-box; margin: 0; padding: 0; }
  html, body {
    width: 1200px; height: 1200px; overflow: hidden;
    background: var(--backdrop);
    font-family: "Roboto", Arial, sans-serif;
    color: var(--ink);
  }
  .card {
    position: absolute; left: 213px; width: 774px; height: 442px;
    background: var(--card);
    box-shadow: 0 6px 18px rgba(0,0,0,0.25);
  }
  .card--front { top: 149px; }
  .card--back  { top: 633px; }

  .brand-name {
    position: absolute; text-align: center;
    font-weight: 700; text-transform: uppercase;
    line-height: 1.05; letter-spacing: 0.5px; color: var(--ink);
  }
  .card--front .brand-name { left: 57px; width: 300px; top: 170px; font-size: 36px; }
  .card--back .brand-name  { left: 0; width: 100%; top: 170px; font-size: 40px; }

  .divider {
    position: absolute; left: 389px; top: 127px;
    width: 2px; height: 179px; background: var(--ink);
  }
  .contact { position: absolute; left: 425px; top: 136px; }
  .contact__name { font-size: 27px; font-weight: 500; line-height: 1.2; }
  .contact__title { font-size: 17px; color: var(--ink-soft); margin-top: 2px; }
  .contact__list { list-style: none; margin-top: 26px; }
  .contact__item {
    display: flex; align-items: center; gap: 8px;
    font-size: 17px; color: var(--ink-soft); height: 28px;
  }
  .contact__item svg { width: 16px; height: 16px; flex: none; }

  .social-row {
    position: absolute; left: 0; right: 0; top: 384px;
    display: flex; align-items: center; gap: 16px;
  }
  .social-row__rule { flex: 1; height: 2px; background: var(--ink); }
  .social-row__list { display: flex; gap: 14px; list-style: none; }
  .social-row__item { font-size: 13px; font-weight: 500; color: var(--ink); }
</style>
</head>
<body>
  <section class="card card--front">
    <div class="brand-name">Brightwave<br>Reach</div>
    <div class="divider"></div>
    <div class="contact">
      <p class="contact__name">Marcus Ellery</p>
      <p class="contact__title">President &amp; CEO</p>
      <ul class="contact__list">
        <li class="contact__item">
          <svg viewBox="0 0 16 16" fill="none" stroke="#fff" stroke-width="1.2"><path d="M3 1.5l2.5 0 1 3.5-1.6 1.2a8 8 0 0 0 4.9 4.9L11 9.5l3.5 1v2.5c0 .8-.7 1.5-1.5 1.5C6.9 14.5 1.5 9.1 1.5 3c0-.8.7-1.5 1.5-1.5z"/></svg>
          604-392-5108
        </li>
        <li class="contact__item">
          <svg viewBox="0 0 16 16" fill="none" stroke="#fff" stroke-width="1.2"><rect x="1.5" y="3.5" width="13" height="9"/><path d="M1.5 3.5l6.5 5 6.5-5"/></svg>
          info@brightwavereach.ca
        </li>
        <li class="contact__item">
          <svg viewBox="0 0 16 16" fill="none" stroke="#fff" stroke-width="1.2"><circle cx="8" cy="8" r="6.5"/><ellipse cx="8" cy="8" rx="2.8" ry="6.5"/><path d="M1.5 8h13M2.5 4.8h11M2.5 11.2h11"/></svg>
          www.brightwavereach.ca
        </li>
      </ul>
    </div>
  </section>

  <section class="card card--back">
    <div class="brand-name">Brightwave<br>Reach</div>
    <div class="social-row">
      <span class="social-row__rule"></span>
      <ul class="social-row__list">
        <li class="social-row__item">Kinloop</li>
        <li class="social-row__item">Linkra</li>
        <li class="social-row__item">Chirpo</li>
        <li class="social-row__item">Voxly</li>
      </ul>
      <span class="social-row__rule"></span>
    </div>
  </section>
</body>
</html>
```